Business Consultancy Business Card Design

Business Card design required for Business Analysis and Project Consultancy business based in Scotland.

Company Name - Brackwell Consulting

Back - Company Logo

Front Details

Euan Brackwell
07402 916 254
euan.brackwell@brackwellconsulting.example
http://www.brackwellconsulting.example

Colours should match the logo colours but I am open to design ideas.

```html
<!DOCTYPE html>
<html lang="en">
<head>
<meta charset="utf-8">
<title>Brackwell Consulting – Business Cards</title>
<link rel="stylesheet" href="https://fonts.googleapis.com/css2?family=Questrial&display=swap">
<style>
  :root {
    --brand-blue: #0b9bdc;
    --brand-green: #6ab23e;
    --text-grey: #55585c;
    --text-dark: #3a3c3f;
    --rule-green: #9ccb7f;
    --card-white: #ffffff;
    --page-bg: #e9eaeb;
  }
  * { margin: 0; padding: 0; box-sizing: border-box; }
  html, body {
    width: 1200px;
    height: 1200px;
    overflow: hidden;
    background: var(--page-bg);
    font-family: "Questrial", sans-serif;
  }
  .card {
    position: absolute;
    left: 220px;
    width: 760px;
    height: 416px;
    background: var(--card-white);
    box-shadow: 0 6px 18px rgba(0,0,0,0.18);
    overflow: hidden;
  }
  .card--front { top: 154px; }
  .card--back  { top: 630px; }

  /* Front card */
  .front-stripe {
    position: absolute;
    left: 30px;
    top: 0;
    width: 84px;
    height: 100%;
    background: var(--brand-blue);
  }
  .front-stripe__top {
    position: absolute;
    left: 0; top: 0;
    width: 100%;
    height: 95px;
    background: var(--brand-green);
  }
  .brand-dot {
    position: absolute;
    left: 42px;
    top: 88px;
    width: 60px;
    height: 60px;
    border-radius: 50%;
    background: var(--card-white);
  }
  .brand-divider {
    position: absolute;
    left: 126px;
    top: 92px;
    width: 2px;
    height: 56px;
    background: var(--text-grey);
  }
  .company-name {
    position: absolute;
    left: 144px;
    top: 98px;
    font-size: 38px;
    letter-spacing: 0.2px;
    color: var(--text-grey);
    white-space: nowrap;
  }
  .person-name {
    position: absolute;
    left: 124px;
    top: 192px;
    font-size: 31px;
    color: var(--brand-blue);
  }
  .name-rule {
    position: absolute;
    left: 124px;
    top: 236px;
    width: 600px;
    height: 1px;
    background: var(--rule-green);
  }
  .contact-list {
    position: absolute;
    left: 78px;
    top: 276px;
    list-style: none;
  }
  .contact-list li {
    display: flex;
    align-items: center;
    height: 27px;
    font-size: 21px;
    color: var(--text-dark);
  }
  .contact-icon {
    width: 20px;
    height: 20px;
    margin-right: 26px;
    flex: none;
  }

  /* Back card */
  .back-frame {
    position: absolute;
    inset: 0;
  }
  .back-mark {
    position: absolute;
    left: 8px;
    top: 34px;
    width: 716px;
    height: 348px;
    display: flex;
    flex-direction: column;
    align-items: center;
    justify-content: center;
    gap: 34px;
  }
  .back-mark__dot {
    width: 100px;
    height: 100px;
    border-radius: 50%;
    background: var(--brand-blue);
  }
  .back-mark__name {
    font-size: 40px;
    color: var(--text-grey);
    white-space: nowrap;
  }
</style>
</head>
<body>

<section class="card card--front" aria-label="Business card front">
  <div class="front-stripe">
    <div class="front-stripe__top"></div>
  </div>
  <div class="brand-dot"></div>
  <div class="brand-divider"></div>
  <p class="company-name">BRACKWELL CONSULTING</p>
  <p class="person-name">Euan Brackwell</p>
  <div class="name-rule"></div>
  <ul class="contact-list">
    <li>
      <svg class="contact-icon" viewBox="0 0 20 20" aria-hidden="true">
        <rect width="20" height="20" rx="3" fill="#6ab23e"/>
        <path d="M6 4.5 L8.2 4.5 L9 7.5 L7.6 8.6 Q8.8 11.2 11.4 12.4 L12.5 11 L15.5 11.8 L15.5 14 Q15.5 15.5 14 15.5 Q5 14.8 4.5 6 Q4.5 4.5 6 4.5 Z" fill="#fff"/>
      </svg>
      07402 916 254
    </li>
    <li>
      <svg class="contact-icon" viewBox="0 0 20 20" aria-hidden="true">
        <rect width="20" height="20" rx="3" fill="#6ab23e"/>
        <circle cx="10" cy="10" r="5.5" fill="none" stroke="#fff" stroke-width="1.6"/>
        <circle cx="10" cy="10" r="2.2" fill="none" stroke="#fff" stroke-width="1.6"/>
      </svg>
      euan.brackwell@brackwellconsulting.example
    </li>
    <li>
      <svg class="contact-icon" viewBox="0 0 20 20" aria-hidden="true">
        <rect width="20" height="20" rx="3" fill="#6ab23e"/>
        <circle cx="10" cy="10" r="6" fill="none" stroke="#fff" stroke-width="1.4"/>
        <ellipse cx="10" cy="10" rx="2.6" ry="6" fill="none" stroke="#fff" stroke-width="1.2"/>
        <line x1="4" y1="10" x2="16" y2="10" stroke="#fff" stroke-width="1.2"/>
      </svg>
      http://www.brackwellconsulting.example
    </li>
  </ul>
</section>

<section class="card card--back" aria-label="Business card back">
  <svg class="back-frame" viewBox="0 0 760 416" aria-hidden="true">
    <rect width="760" height="416" fill="#6ab23e"/>
    <rect x="0" y="0" width="760" height="34" fill="#0b9bdc"/>
    <rect x="0" y="0" width="8" height="382" fill="#0b9bdc"/>
    <rect x="8" y="34" width="716" height="348" fill="#ffffff"/>
  </svg>
  <div class="back-mark">
    <div class="back-mark__dot"></div>
    <p class="back-mark__name">BRACKWELL CONSULTING</p>
  </div>
</section>

</body>
</html>
```